Alder Hollow Family Dentistry
business card
Alder Hollow Family Dentistry -
Creative Brief
Simple
Dr. Owen T. Farrow, D.M.D.
2817 Juniper Ln. Ste. C Cedar Vale, ID 84561
drfarrow@alderhollowfamilydentistry.example
www.alderhollowfamilydentistry.example

```html
<!DOCTYPE html>
<html lang="en">
<head>
<meta charset="utf-8">
<title>Alder Hollow Family Dentistry – Business Card</title>
<link rel="stylesheet" href="https://fonts.googleapis.com/css2?family=Cinzel:wght@600&family=Arimo:wght@400&display=swap">
<style>
  :root {
    --canvas: #ffffff;
    --card-white: #ffffff;
    --card-edge: #cfcfcf;
    --brand-green: #2ea043;
    --swoosh-green: #3aa63c;
    --swoosh-light: #8ccf3f;
    --text-dark: #222222;
    --wordmark: #34404a;
    --blue-deep: #1c64b4;
    --blue-light: #d8e9f8;
    --green-deep: #44a52f;
    --green-light: #a2d84a;
  }
  * { box-sizing: border-box; margin: 0; padding: 0; }
  html, body { width: 1200px; height: 754px; overflow: hidden; }
  body { background: var(--canvas); position: relative; font-family: "Arimo", Arial, sans-serif; }

  .card {
    position: absolute;
    width: 564px;
    height: 330px;
    border: 1px solid var(--card-edge);
    overflow: hidden;
  }
  .card--front { left: 29px; top: 29px; background: var(--card-white); }
  .card--blue  { left: 607px; top: 29px; background: radial-gradient(ellipse 60% 70% at 50% 40%, var(--blue-light) 0%, #7fb2e4 45%, var(--blue-deep) 100%); }
  .card--green { left: 29px; top: 377px; background: linear-gradient(160deg, var(--green-light) 0%, #6fc036 50%, var(--green-deep) 100%); }
  .card--plain { left: 607px; top: 377px; background: var(--card-white); }

  .wordmark {
    position: absolute;
    display: flex;
    align-items: center;
    gap: 12px;
    font-family: "Cinzel", Georgia, serif;
    font-weight: 600;
    color: var(--wordmark);
    line-height: 1.1;
    white-space: nowrap;
  }
  .wordmark__dot { flex: none; border-radius: 50%; background: var(--wordmark); }
  .wordmark__name { display: block; }

  .card--front .wordmark { left: 22px; top: 68px; font-size: 22px; }
  .card--front .wordmark__dot { width: 13px; height: 13px; }

  .card--blue .wordmark,
  .card--green .wordmark { left: 50%; top: 50%; transform: translate(-50%, -50%); font-size: 26px; }
  .card--blue .wordmark__dot,
  .card--green .wordmark__dot { width: 15px; height: 15px; }

  .card--plain .wordmark { left: 50%; top: 50%; transform: translate(-50%, -50%); font-size: 30px; }
  .card--plain .wordmark__dot { width: 18px; height: 18px; }

  .doctor {
    position: absolute;
    left: 108px;
    top: 180px;
    font-size: 19px;
    color: var(--brand-green);
    white-space: nowrap;
  }
  .contact {
    position: absolute;
    left: 20px;
    top: 226px;
    font-size: 12px;
    line-height: 16px;
    color: var(--text-dark);
    list-style: none;
    white-space: nowrap;
  }
  .contact .label, .contact .web { color: var(--brand-green); }

  .swoosh { position: absolute; left: 0; bottom: 0; width: 564px; height: 120px; }
</style>
</head>
<body>

  <section class="card card--front" aria-label="Card front">
    <div class="wordmark">
      <span class="wordmark__dot"></span>
      <span class="wordmark__name">Alder Hollow<br>Family Dentistry</span>
    </div>
    <p class="doctor">Dr. Owen T. Farrow, D.M.D.</p>
    <ul class="contact">
      <li>2817 Juniper Ln. Ste. C, Cedar Vale, ID 84561</li>
      <li><span class="label">Phone:</span> 208-555-0142 | <span class="label">Fax:</span> 208-555-0187</li>
      <li><span class="label">Email:</span> drfarrow@alderhollowfamilydentistry.example</li>
      <li class="web">www.alderhollowfamilydentistry.example</li>
    </ul>
    <svg class="swoosh" viewBox="0 0 564 120" preserveAspectRatio="none" aria-hidden="true">
      <defs>
        <linearGradient id="swooshFill" x1="0" y1="1" x2="1" y2="0">
          <stop offset="0" stop-color="#3aa63c"/>
          <stop offset="1" stop-color="#8ccf3f"/>
        </linearGradient>
      </defs>
      <path d="M0 118 C180 112 400 85 564 0 L564 120 L0 120 Z" fill="url(#swooshFill)"/>
      <path d="M0 108 C200 104 410 78 564 8" fill="none" stroke="#8ccf3f" stroke-width="2"/>
    </svg>
  </section>

  <section class="card card--blue" aria-label="Card back, blue">
    <div class="wordmark">
      <span class="wordmark__dot"></span>
      <span class="wordmark__name">Alder Hollow<br>Family Dentistry</span>
    </div>
  </section>

  <section class="card card--green" aria-label="Card back, green">
    <div class="wordmark">
      <span class="wordmark__dot"></span>
      <span class="wordmark__name">Alder Hollow<br>Family Dentistry</span>
    </div>
  </section>

  <section class="card card--plain" aria-label="Card back, white">
    <div class="wordmark">
      <span class="wordmark__dot"></span>
      <span class="wordmark__name">Alder Hollow<br>Family Dentistry</span>
    </div>
  </section>

</body>
</html>
```